Bellcove Realty Business Cards
Business Cards design
Professional
Marnie Toskovic
Licensed Broker
482 Linwell Ave
San Francisco, CA 94387
marnie@bellcoverealty.com
www.bellcoverealty.com
DRE#07391826
Include photo on front of card
- Experienced Mortgage Consultant
- Residential Listings
- Short Sale Expertise
- Property Management
Logo
Headshot

```html
<!DOCTYPE html>
<html lang="en">
<head>
<meta charset="utf-8">
<title>Bellcove Realty Business Cards</title>
<link rel="stylesheet" href="https://fonts.googleapis.com/css2?family=Arimo:wght@400;700&family=Tinos&display=swap">
<style>
  :root {
    --bg: #e4e2df;
    --card-white: #ffffff;
    --card-grey: #f1f1f2;
    --blue-dark: #1b3a8c;
    --blue: #2c5cc5;
    --gold: #f2b51c;
    --red: #c9302c;
    --ink: #333a44;
    --muted: #6b7280;
    --accent: #e46a3a;
    --orange-light: #ffd84a;
    --orange-deep: #f59a1c;
    --photo: #b8877a;
  }
  * { box-sizing: border-box; margin: 0; padding: 0; }
  html, body { width: 1200px; height: 826px; overflow: hidden; }
  body { background: var(--bg); position: relative; font-family: "Arimo", Arial, sans-serif; color: var(--ink); }

  .card {
    position: absolute; width: 480px; height: 276px; overflow: hidden;
    box-shadow: 0 6px 18px rgba(0,0,0,.25);
  }

  /* Front */
  .card-front { left: 90px; top: 120px; background: var(--card-white); }
  .card-front .panel { position: absolute; inset: 0; }
  .brand { position: absolute; left: 24px; top: 26px; display: flex; align-items: center; gap: 8px; }
  .brand-mark { width: 16px; height: 16px; background: var(--red); flex: none; }
  .brand-name { font-weight: 700; font-size: 20px; line-height: 21px; color: var(--blue-dark); letter-spacing: .5px; }
  .address { position: absolute; left: 24px; top: 108px; font-size: 10.5px; line-height: 14px; color: var(--muted); }
  .contacts { position: absolute; left: 24px; top: 152px; font-size: 10.5px; line-height: 14px; color: var(--muted); }
  .contacts dt { float: left; width: 36px; clear: left; }
  .contacts dd { margin-left: 36px; }
  .license { position: absolute; left: 24px; top: 232px; font-size: 12px; font-weight: 700; color: var(--blue-dark); }
  .photo {
    position: absolute; left: 300px; top: 36px; width: 90px; height: 112px;
    border: 4px solid var(--gold);
    background: linear-gradient(180deg, #e9b24a 0%, var(--photo) 55%, #c2353a 100%);
  }
  .agent { position: absolute; left: 270px; width: 150px; top: 158px; text-align: center; color: #fff; }
  .agent-name { font-weight: 700; font-size: 15px; }
  .agent-title { font-size: 11px; margin-top: 3px; opacity: .9; }

  /* Backs */
  .services { list-style: none; font-family: "Tinos", "Times New Roman", serif; font-size: 19px; line-height: 27px; }
  .services li::before { content: "›"; color: var(--accent); margin-right: 10px; font-family: "Arimo", Arial, sans-serif; font-weight: 700; }
  .web { position: absolute; right: 22px; bottom: 18px; font-size: 10px; color: var(--ink); }

  .card-back { left: 630px; top: 140px; background: linear-gradient(180deg, var(--card-white) 0%, var(--card-grey) 100%); }
  .card-back .services { position: absolute; left: 30px; top: 42px; color: var(--ink); }
  .rule { position: absolute; left: 50px; right: 22px; bottom: 36px; height: 2px; background: var(--accent); }
  .rule-mark { position: absolute; left: 50px; bottom: 40px; width: 16px; height: 16px; background: var(--accent); }

  .card-alt { left: 360px; top: 460px; background: radial-gradient(circle at 30% 40%, var(--orange-light) 0%, var(--orange-deep) 100%); }
  .card-alt .services { position: absolute; left: 30px; top: 30px; color: #6b3a10; }
  .card-alt .services li::before { color: #fff; }
  .card-alt .rule { background: #fff; }
  .card-alt .rule-mark { background: #fff; }
  .card-alt .web { color: #6b3a10; }
</style>
</head>
<body>

<section class="card card-front" aria-label="Business card front">
  <svg class="panel" viewBox="0 0 480 276" preserveAspectRatio="none" aria-hidden="true">
    <defs>
      <linearGradient id="blueFill" x1="0" y1="0" x2="1" y2="1">
        <stop offset="0" stop-color="var(--blue)"/>
        <stop offset="1" stop-color="var(--blue-dark)"/>
      </linearGradient>
    </defs>
    <path d="M190,0 L480,0 L480,276 L250,276 C228,190 212,96 190,0 Z" fill="var(--gold)"/>
    <path d="M204,0 L480,0 L480,276 L264,276 C242,190 226,96 204,0 Z" fill="url(#blueFill)"/>
  </svg>

  <div class="brand">
    <span class="brand-mark"></span>
    <span class="brand-name">BELLCOVE<br>REALTY</span>
  </div>

  <p class="address">482 Linwell Ave<br>San Francisco, CA 94387</p>

  <dl class="contacts">
    <dt>Cell</dt><dd>415-555-0142</dd>
    <dt>Fax</dt><dd>415-555-0187</dd>
    <dt>Email</dt><dd>marnie@bellcoverealty.com</dd>
    <dt>Web</dt><dd>www.bellcoverealty.com</dd>
  </dl>

  <p class="license">DRE# 07391826</p>

  <div class="photo" role="img" aria-label="Headshot of Marnie Toskovic"></div>
  <div class="agent">
    <p class="agent-name">Marnie Toskovic</p>
    <p class="agent-title">Licensed Broker</p>
  </div>
</section>

<section class="card card-back" aria-label="Business card back, white">
  <ul class="services">
    <li>Experienced Mortgage Consultant</li>
    <li>Residential Listings</li>
    <li>Short Sale Expertise</li>
    <li>Property Management</li>
  </ul>
  <span class="rule-mark"></span>
  <span class="rule"></span>
  <p class="web">www.bellcoverealty.com</p>
</section>

<section class="card card-alt" aria-label="Business card back, orange">
  <ul class="services">
    <li>Experienced Mortgage Consultant</li>
    <li>Residential Listings</li>
    <li>Short Sale Expertise</li>
    <li>Property Management</li>
  </ul>
  <span class="rule-mark"></span>
  <span class="rule"></span>
  <p class="web">www.bellcoverealty.com</p>
</section>

</body>
</html>
```